International MLM Business needs Coffee Packaging Design

We are an MLM Company engaged in selling Food Supplements to our independent distributors.

We need a Packaging Design for our Instant Coffee (Cafe Latte) enhanced with Food Supplement (Ganoderma and Goji Powder)

Sachet Material is PET/AL/PE
Sachet Size is 45mm x 160mm (L x H) (FORMED)
Canvass Size is 110mm x 160mm (L x H) (FLAT)

The packaging design requirements are as follows:

1. Design must be in upright position (portrait).

2. We would like to see "VELTORIS" (our brand logo) included in the design. See uploaded file.

3. We also would like to see some "gold" touch in the label.

4. The coffee is part of our "SUPER" series.

5. Include "PREMIUM COFFEE", "WITH GANODERMA & GOJI EXTRACT" as our main selling point.

6. Add Net Weight at the lower right portion. Net Weight is 25 grams.

7. Add Serving Instruction at the Back.

1. Empty 1 sachet of VELTORIS Super Cafe Latte into a mug.
2. Fill the mug with 220ml of hot water (80 degrees celsius) and stir. (Use "80oc")
I don't know how to superscript the "o".
3. Enjoy a rich, healthy VELTORIS Super Cafe Latte.

8. Add Ingredients at the Back.

"Sugar, Non Dairy Creamer, Pure Instant Coffee, Organic Goji Extract, Organic Ganoderma Extract."

9. Add Best Before Date at the Back.

10. Add Manufacturer Details at the Back.

Our website is http://www.veltoris-example.com

*attached photo is for presentation purposes only. It's up to you to design.*

Designer Payment changed to committed. We are very serious about this project. So please kindly submit all entries. Thanks!

```html
<!DOCTYPE html>
<html lang="en">
<head>
<meta charset="utf-8">
<title>Veltoris Super Cafe Latte – Sachet Front and Back</title>
<link rel="stylesheet" href="https://fonts.googleapis.com/css2?family=Lobster&family=Oswald:wght@500;600&family=Patrick+Hand&family=Open+Sans:wght@400;700&display=swap">
<style>
  :root {
    --bg: #3d3d3d;
    --bg-light: #5a5a5a;
    --brown-dark: #3a1d10;
    --brown: #5a2e17;
    --brown-mid: #7a4424;
    --cream: #f3ead3;
    --cream-light: #fbf6e8;
    --cream-shade: #e6d7b4;
    --gold: #d9b13b;
    --gold-dark: #a77b2a;
    --gold-light: #f2d98a;
    --ink: #4a2413;
  }
  * { box-sizing: border-box; margin: 0; padding: 0; }
  html, body { width: 910px; height: 1200px; overflow: hidden; }
  body {
    background: radial-gradient(ellipse at 50% 35%, var(--bg-light), var(--bg) 75%);
    font-family: "Open Sans", sans-serif;
    position: relative;
  }

  .sachet {
    position: absolute;
    top: 90px;
    width: 310px;
    height: 1010px;
    border-radius: 10px;
    overflow: hidden;
    background: var(--cream);
    box-shadow: 0 18px 40px rgba(0,0,0,.45);
  }
  .sachet--front { left: 115px; }
  .sachet--back  { left: 485px; }

  .crimp {
    position: absolute; left: 0; right: 0; height: 46px;
    background: repeating-linear-gradient(to bottom, rgba(255,255,255,.14) 0 2px, transparent 2px 7px);
  }
  .crimp--top { top: 0; }
  .crimp--bottom { bottom: 0; }

  /* brown cap */
  .cap {
    position: absolute; left: 0; right: 0; top: 0;
    background: linear-gradient(90deg, var(--brown-dark), var(--brown-mid) 45%, var(--brown) 70%, var(--brown-dark));
  }
  .sachet--front .cap { height: 300px; }
  .sachet--back .cap { height: 290px; }

  .gold-band {
    position: absolute; left: 0; right: 0; height: 14px;
    background: linear-gradient(90deg, var(--gold-dark), var(--gold-light) 50%, var(--gold-dark));
  }
  .gold-band::after {
    content: ""; position: absolute; left: 0; right: 0; bottom: -6px; height: 2px;
    background: var(--gold-dark);
  }
  .sachet--front .gold-band--top { top: 300px; }
  .sachet--back .gold-band--top { top: 290px; }

  .brand {
    position: absolute; left: 0; right: 0; top: 100px;
    display: flex; flex-direction: column; align-items: center; gap: 16px;
  }
  .brand__dot {
    width: 86px; height: 86px; border-radius: 50%; background: var(--gold);
  }
  .brand__name {
    font-family: "Open Sans", sans-serif; font-weight: 400;
    font-size: 27px; color: var(--gold); letter-spacing: .5px;
  }

  /* front body */
  .front-body {
    position: absolute; left: 0; right: 0; top: 320px; bottom: 60px;
    background: radial-gradient(ellipse at 75% 30%, var(--cream-shade), var(--cream) 55%, var(--cream-light));
  }
  .product-name {
    position: absolute; top: 28px; left: 0; right: 0; text-align: center;
    font-family: "Lobster", cursive; font-size: 56px; color: var(--ink);
    letter-spacing: -1px;
  }
  .product-tag {
    position: absolute; top: 118px; left: 0; right: 0; text-align: center;
    font-family: "Oswald", sans-serif; font-weight: 600; font-size: 27px; color: var(--ink);
  }
  .product-extract {
    position: absolute; top: 162px; left: 0; right: 0; text-align: center;
    font-family: "Patrick Hand", cursive; font-size: 23px; line-height: 1.15; color: var(--brown-dark);
  }
  .cup-art {
    position: absolute; left: 60px; top: 240px; width: 210px; height: 330px;
    border-radius: 40% 40% 48% 48%;
    background: radial-gradient(ellipse at 50% 70%, #9b6a49, #c9a685 60%, rgba(243,234,211,0) 72%);
  }
  .seal {
    position: absolute; left: 20px; top: 420px; width: 58px; height: 58px; border-radius: 50%;
    background: radial-gradient(circle, var(--brown) 55%, var(--gold-dark) 58%, var(--gold) 100%);
  }
  .net-weight {
    position: absolute; right: 16px; bottom: 14px;
    font-family: "Open Sans", sans-serif; font-size: 15px; color: var(--ink);
  }
  .net-weight strong { font-size: 21px; font-weight: 700; }

  .foot {
    position: absolute; left: 0; right: 0; bottom: 0; height: 60px;
    background: linear-gradient(90deg, var(--gold-dark), var(--gold-light) 45%, var(--gold) 70%, var(--gold-dark));
  }

  /* back body */
  .back-body {
    position: absolute; left: 0; right: 0; top: 310px; bottom: 60px;
    padding: 30px 26px 0;
    color: var(--ink);
    font-size: 14px; line-height: 1.3;
  }
  .back-heading {
    font-family: "Oswald", sans-serif; font-weight: 500; font-size: 17px; letter-spacing: .3px;
    margin-bottom: 6px;
  }
  .steps { list-style: none; }
  .steps li { display: flex; gap: 8px; margin-bottom: 5px; }
  .step-num {
    flex: none; width: 20px; height: 20px; border-radius: 50%;
    background: var(--brown); color: var(--cream-light);
    font-size: 12px; font-weight: 700; display: flex; align-items: center; justify-content: center;
  }
  .ingredients { margin-top: 10px; }
  .ingredients p { margin-top: 2px; }
  .steps-art {
    margin: 26px auto 0; width: 240px; height: 80px; border-radius: 8px;
    background: linear-gradient(90deg, #e9dcc0, #d8c3a0, #e9dcc0);
  }
  .dates {
    margin-top: 26px; font-family: "Patrick Hand", cursive; font-size: 19px; line-height: 1.25;
  }
  .maker { margin-top: 30px; font-size: 14px; }
  .maker strong { display: block; font-size: 17px; }
  .website { margin-top: 6px; font-weight: 700; font-size: 14px; letter-spacing: .3px; }
</style>
</head>
<body>

  <section class="sachet sachet--front" aria-label="Sachet front">
    <div class="cap">
      <div class="crimp crimp--top"></div>
      <div class="brand">
        <span class="brand__dot"></span>
        <span class="brand__name">veltoris-example</span>
      </div>
    </div>
    <div class="gold-band gold-band--top"></div>
    <div class="front-body">
      <h1 class="product-name">Cafe Latte</h1>
      <p class="product-tag">PREMIUM COFFEE</p>
      <p class="product-extract">with ganoderma<br>&amp; goji extract</p>
      <div class="cup-art" role="img" aria-label="Illustration of a steaming coffee cup on a saucer"></div>
      <div class="seal" role="img" aria-label="Premium quality seal"></div>
      <p class="net-weight">Net W <strong>25</strong> gms.</p>
    </div>
    <div class="foot"><div class="crimp crimp--bottom"></div></div>
  </section>

  <section class="sachet sachet--back" aria-label="Sachet back">
    <div class="cap"><div class="crimp crimp--top"></div></div>
    <div class="gold-band gold-band--top"></div>
    <div class="back-body">
      <h2 class="back-heading">SERVING INSTRUCTION</h2>
      <ol class="steps">
        <li><span class="step-num">1</span><span>Empty 1 sachet of VELTORIS Super Cafe Latte into a mug.</span></li>
        <li><span class="step-num">2</span><span>Fill the mug with 220ml of hot water (80 degrees celsius)</span></li>
        <li><span class="step-num">3</span><span>Enjoy a rich, healthy VELTORIS Super Cafe Latte.</span></li>
      </ol>
      <div class="ingredients">
        <h2 class="back-heading">INGREDIENTS</h2>
        <p>“Sugar, Non Dairy Creamer, Pure Instant Coffee, Organic Goji Extract, Organic Ganoderma Extract”</p>
      </div>
      <div class="steps-art" role="img" aria-label="Three small drawings showing pouring, filling and stirring the mug"></div>
      <p class="dates">Best before Dec 2015<br>Best before Dec 2015</p>
      <p class="maker">Manufacturer by:<strong>Company Name Here</strong></p>
      <p class="website">www.veltoris-example.com</p>
    </div>
    <div class="foot"><div class="crimp crimp--bottom"></div></div>
  </section>

</body>
</html>
```